Visually Compelling Flyer Design - Orvane Benefits

We are a life insurance company looking to create visually compelling flyers that gain attention of potential buyers and simplify the concept. It should be professional, friendly, approachable in nature. Our logo and several rough drafts are included.
We are looking to refine this look and make it ultra professional, clean and easy to follow. A creative brief with brand guidelines is also included.
FLYER 1 — PAY YOURSELF FIRST
EYEBROW TAG
YOUR COMPANY JUST UPGRADED YOUR BENEFITS
HEADLINE
One small decision. A lifetime of protection.
SUBHEADLINE
Permanent life insurance + long-term care coverage, starting at $1 a day.
EYEBROW TAG
CHOOSE YOUR DAILY INVESTMENT
STAT — TIER 1
$1 / day → $20,000 Life Insurance
STAT — TIER 2 (HERO — make this one biggest/most prominent)
$2 / day → $40,000 Life Insurance
★ Most Popular
STAT — TIER 3
$3 / day → $60,000 Life Insurance
CAPTION
Rate locked at enrollment. Benefit never decreases.
EYEBROW TAG
THREE BENEFITS. ONE POLICY.
SUBHEADLINE
Your money works three ways.
CALLOUT — BENEFIT 1
01 | Cash Value Growth
BODY
Averages 6% annually over the last 50 years — guaranteed never to fall below 3%. Better than any savings account. And if you ever need it, you can borrow against it. It's your money.
CALLOUT — BENEFIT 2
02 | Tax-Free Death Benefit
BODY
From day one, your family is protected. The full benefit is paid tax-free to the person you choose — no waiting period, no exceptions. That's your legacy, preserved.
CALLOUT — BENEFIT 3
03 | Long-Term Care Coverage
BODY
70% of Americans will need long-term care. This plan pays 75% of your benefit — upfront and tax-free — to cover those costs while you're still alive. Your retirement savings stay intact. Your family stays protected.
EYEBROW TAG
ALREADY HAVE LIFE INSURANCE THROUGH WORK?
SUBHEADLINE
That's term. It ends when you need it most.
BODY
Term life insurance is designed for temporary needs — protecting your paycheck, your mortgage, your kids while they're home. When you retire, the house is paid off and your children are grown. Term ends because the need ends.
BODY
But one need never ends: your final expenses and the cost of long-term care. This permanent plan stays with you after retirement — when term coverage is gone and getting new coverage is expensive or impossible.
COMPARISON — LEFT COLUMN HEADER
✕ TERM LIFE
COMPARISON — LEFT COLUMN ITEMS
Gets more expensive with age
Ends at retirement
No cash value
Temporary protection only
COMPARISON — RIGHT COLUMN HEADER
✓ THIS PLAN
COMPARISON — RIGHT COLUMN ITEMS
Rate locked forever at enrollment
Stays with you after retirement
Builds real cash value
Permanent protection for life
EYEBROW TAG
WHAT MAKES THIS DIFFERENT
SUBHEADLINE
Built for you. Stays with you.
CALLOUT
✓ Guaranteed Issued
No medical exams. No questions asked. You qualify.
CALLOUT
✓ Group Rate
Because you work here, you get pricing individuals can't access on their own.
CALLOUT
✓ Rate Locked Forever
Your premium never increases. Your benefit never decreases.
CALLOUT
✓ Portable
Change jobs. Retire. Your policy comes with you at the same rate.
CALLOUT
✓ Family Coverage
Protect your spouse and children under the same plan.
SUBHEADLINE
Protect retirement. Preserve dignity. Plan ahead.
CTA
Be on the lookout for your personalized coverage details.
CAPTION
Brokered by Orvane Benefits · Underwritten by TrelloraLife
FLYER 2 — THE LONG-TERM CARE REALITY
EYEBROW TAG
WHAT MOST PEOPLE DON'T KNOW — BUT SHOULD
HEADLINE
Most Americans are unprepared. You don't have to be.
SUBHEADLINE
The long-term care gap is real — and it affects families like yours.
EYEBROW TAG
THE NUMBERS ARE HARD TO IGNORE
STAT
70%
of Americans age 65 and older will need some form of long-term care during their lifetime.
CAPTION
Source: Pike & Marsden, Review of Elder Welfare and Civic Planning, 2018
STAT
3–4%
of Americans over 50 own a private long-term care insurance policy. The gap between who needs it and who has it is staggering.
CAPTION
Source: Dunn & Solberg, QRT Wellness Wire, 2023
STAT
$700 Billion+
Estimated annual U.S. long-term care cost — and it's growing every year.
CAPTION
Source: Brandt Lowe & Petrasek, Civic Policy Roundtable, 2020
STAT
$470 Billion
The estimated value of unpaid care provided by family members every year. That's the real cost — measured in time, stress, and financial sacrifice.
CAPTION
Source: Lindqvist & Oram, Harborline Institute
STAT
80%
of total long-term care spending goes directly to assist retirees. This isn't a young person's problem. But the time to plan is now.
CAPTION
SUBHEADLINE
Long-term care doesn't just cost money. It costs families.
BODY
When there's no plan in place, the people you love absorb the impact — financially, emotionally, and physically. Retirement savings built over a lifetime can disappear in months. Family members step back from their own lives to provide care. Dignity becomes a daily negotiation.
BODY
This is not inevitable. A small decision today changes the entire outcome.
EYEBROW TAG
THE SOLUTION
HEADLINE
The Pay Yourself First Principle.
BODY
Take the first $1, $2, or $3 you make every day and invest it in a permanent life insurance policy that includes long-term care coverage — underwritten by TrelloraLife, offered through your employer at a group rate, and Guaranteed Issued for everyone.
STAT
$1 / day → $20,000 $2 / day → $40,000 $3 / day → $60,000
BODY
The benefit includes three protections in one: a cash value that grows at an average of 6% annually, a tax-free death benefit for your family, and long-term care coverage that pays 75% of your benefit upfront — tax-free — when you need care most.
SUBHEADLINE
Whether you're single, married, with children or without — there is protection in this plan for you.
HEADLINE
CTA
Look for your personalized offer. Coverage details are coming your way.
CAPTION
COPY RULES FOR DESIGNERS
Headlines are one idea only. Never more than two lines.
Stats stand alone. Never buried in a paragraph.
Body copy maxes at 3 sentences per block. If it's longer, cut it.
The $2/day tier is always the hero. Always.
"Guaranteed Issued" appears on both flyers. It's the most important trust signal.
TrelloraLife is always attributed. Always.
The tagline is: Protect retirement. Preserve dignity. Plan ahead. — Use it verbatim.
Target Market(s)
Average Americans with a family - adults looking for life insurance
Industry/Entity Type
Life Insurance & Financial Retirement

```html
<!DOCTYPE html>
<html lang="en">
<head>
<meta charset="utf-8">
<title>Orvane Benefits — Long-Term Care Flyer</title>
<link rel="stylesheet" href="https://fonts.googleapis.com/css2?family=Manrope:wght@600;700;800&family=Inter:wght@300;400;600;700&display=swap">
<style>
:root{
  --navy:#263f93;
  --teal:#6ccbdd;
  --ink:#141414;
  --paper:#ffffff;
  --stage:#c4c5c9;
}
*{box-sizing:border-box;margin:0;padding:0}
html,body{width:1200px;height:780px;overflow:hidden;background:var(--stage)}
body{position:relative;font-family:"Inter",sans-serif;color:var(--ink)}
.page{position:absolute;top:68px;width:503px;height:650px;background:var(--paper);overflow:hidden;box-shadow:0 2px 10px rgba(0,0,0,.12)}
.page--stats{left:71px}
.page--solution{left:608px}
.abs{position:absolute}
.accent{color:var(--teal)}

/* hero */
.hero{left:0;top:0;width:503px;height:213px;background:var(--navy)}
.hero-photo{left:0;top:0}
.eyebrow{left:0;top:0;height:34px;width:364px;background:var(--teal);border-radius:0 0 6px 0;color:var(--navy);font:800 14.2px/34px "Manrope",sans-serif;padding-left:15px;letter-spacing:-.2px}
.hero-title{left:20px;top:50px;color:#fff;font:700 25.5px/26.5px "Manrope",sans-serif;letter-spacing:-.3px}
.hero-sub{left:20px;top:146px;color:#fff;font:300 15.6px/22px "Inter",sans-serif}

/* brand */
.brand{left:14px;top:240px;width:80px;text-align:center}
.brand-dot{width:56px;height:56px;border-radius:50%;background:var(--teal);margin:6px auto 10px}
.brand-name{color:var(--navy);font:800 17px/18px "Manrope",sans-serif}

.section-title{left:110px;top:232px;color:var(--navy);font:800 21.4px/28px "Manrope",sans-serif;letter-spacing:-.3px;white-space:nowrap}

/* stat cards */
.stat{position:absolute;background:var(--navy);border-radius:9px;color:#fff}
.stat-figure{position:absolute;left:12px;top:11px;width:53px;height:52px;background:#fff;border-radius:6px;color:var(--navy);display:flex;flex-direction:column;align-items:center;justify-content:center;font:700 17px/18px "Manrope",sans-serif}
.stat-figure small{font:700 10px/13px "Inter",sans-serif}
.stat-text{position:absolute;font:400 11.3px/13.8px "Inter",sans-serif}
.stat-source{position:absolute;left:16px;width:205px;font:400 10.6px/13px "Inter",sans-serif}

/* solution page */
.photo{border-radius:14px}
.care-title{left:215px;top:15px;font:700 19.6px/24px "Manrope",sans-serif;letter-spacing:-.2px}
.body{font:400 11.4px/13.75px "Inter",sans-serif}
.tag{left:0;top:205px;width:109px;height:26px;background:var(--teal);border-radius:0 13px 13px 0;color:#fff;font:700 12px/26px "Inter",sans-serif;padding-left:12px}
.solution-title{left:14px;top:238px;font:700 19.2px/26px "Manrope",sans-serif;letter-spacing:-.2px}
.tier{top:441px;width:155px;height:37px;border-radius:19px;background:var(--navy);color:#fff;font:600 14.2px/37px "Inter",sans-serif;text-align:center;white-space:nowrap}
.footer{left:0;top:495px;width:503px;height:155px;background:var(--navy);color:#fff;text-align:center}
.tagline{position:absolute;left:0;right:0;top:12px;font:700 20.4px/26px "Manrope",sans-serif}
.footer-sub{position:absolute;left:0;right:0;top:48px;font:400 13px/17px "Inter",sans-serif}
.cta{position:absolute;left:17px;top:87px;width:470px;height:25px;border-radius:9px;background:var(--teal);color:var(--navy);font:700 13.3px/25px "Manrope",sans-serif}
.footer-note{position:absolute;left:0;right:0;top:122px;font:400 11.5px/14px "Inter",sans-serif}
</style>
</head>
<body>

<section class="page page--stats">
  <div class="abs hero">
    <svg class="abs hero-photo" width="503" height="213" role="img" aria-label="Photo of smiling grandparents playing outdoors with their granddaughter in sunlight">
      <defs>
        <linearGradient id="sunGlow" x1="0" y1="0" x2="1" y2="0">
          <stop offset="0" stop-color="#263f93" stop-opacity="0"/>
          <stop offset=".45" stop-color="#9aa7c9"/>
          <stop offset=".75" stop-color="#c9b39a"/>
          <stop offset="1" stop-color="#6f7d5c"/>
        </linearGradient>
      </defs>
      <path d="M255 0H503V213H270C270 150 250 80 255 0Z" fill="url(#sunGlow)"/>
      <path d="M430 213C470 205 495 185 503 160V176C490 200 470 210 440 213Z" fill="#6ccbdd"/>
    </svg>
    <div class="abs eyebrow">WHAT MOST PEOPLE DON’T KNOW — BUT SHOULD</div>
    <h1 class="abs hero-title">Most Americans are<br><span class="accent">unprepared</span>. You<br>don’t have to be.</h1>
    <p class="abs hero-sub">The long-term care gap is real —<br>and it affects families like yours.</p>
  </div>

  <div class="abs brand">
    <div class="brand-dot"></div>
    <div class="brand-name">Orvane Benefits</div>
  </div>

  <h2 class="abs section-title">THE <span class="accent">NUMBERS</span> ARE HARD TO IGNORE</h2>

  <div class="stat" style="left:107px;top:272px;width:375px;height:84px">
    <div class="stat-figure" style="top:16px">$470<small>Billion+</small></div>
    <p class="stat-text" style="left:79px;top:12px;width:290px">The estimated value of unpaid care provided by family members every year. That's the real cost — measured in time, stress, and financial sacrifice.</p>
    <p class="stat-source" style="left:80px;top:61px;width:285px">Source: Lindqvist &amp; Oram, Harborline Institute</p>
  </div>

  <div class="stat" style="left:16px;top:372px;width:228px;height:119px">
    <div class="stat-figure">70%</div>
    <p class="stat-text" style="left:78px;top:10px;width:145px">of Americans age 65 and older will need some form of long-term care during their lifetime.</p>
    <p class="stat-source" style="top:84px">Source: Pike &amp; Marsden, Review of Elder Welfare and Civic Planning, 2018</p>
  </div>

  <div class="stat" style="left:254px;top:372px;width:228px;height:119px">
    <div class="stat-figure">3–4%</div>
    <p class="stat-text" style="left:78px;top:10px;width:145px">of Americans over 50 own a private long-term care insurance policy. The gap between who needs it and who has it is staggering.</p>
    <p class="stat-source" style="top:86px">Source: Dunn &amp; Solberg, QRT Wellness Wire, 2023</p>
  </div>

  <div class="stat" style="left:16px;top:503px;width:228px;height:120px">
    <div class="stat-figure">$700<small>Billion+</small></div>
    <p class="stat-text" style="left:78px;top:10px;width:140px">Estimated annual U.S. long-term care cost — and it's growing every year.</p>
    <p class="stat-source" style="top:84px">Source: Brandt Lowe &amp; Petrasek, Civic Policy Roundtable, 2020</p>
  </div>

  <div class="stat" style="left:254px;top:503px;width:228px;height:120px">
    <div class="stat-figure">80%</div>
    <p class="stat-text" style="left:78px;top:10px;width:145px">of total long-term care spending goes directly to assist retirees. This isn't a young person's problem. But the time to plan is now.</p>
    <p class="stat-source" style="top:86px">Source: Lindqvist &amp; Oram, Harborline Institute</p>
  </div>
</section>

<section class="page page--solution">
  <div class="abs photo" role="img" aria-label="Photo of a grandfather and young grandson in flat caps in a flowering meadow" style="left:16px;top:17px;width:180px;height:172px;background:linear-gradient(160deg,#9cbf5a 0%,#5f8a2e 55%,#b7c94a 100%)"></div>
  <h2 class="abs care-title"><span class="accent">Long-term care</span> doesn’t just<br>cost money. It costs families.</h2>
  <p class="abs body" style="left:215px;top:73px;width:275px">When there's no plan in place, the people you love absorb the impact — financially, emotionally, and physically. Retirement savings built over a lifetime can disappear in months. Family members step back from their own lives to provide care. Dignity becomes a daily negotiation.</p>
  <p class="abs body" style="left:215px;top:167px;width:275px">This is not inevitable. A small decision today changes the entire outcome.</p>

  <div class="abs tag">THE SOLUTION</div>
  <h2 class="abs solution-title">The Pay Yourself <span class="accent">First Principle.</span></h2>
  <p class="abs body" style="left:17px;top:272px;width:300px">Take the first <b>$1, $2, or $3</b> you make every day and invest it in a permanent life insurance policy that includes long-term care coverage — underwritten by TrelloraLife, offered through your employer at a group rate, and Guaranteed Issued for everyone.</p>
  <p class="abs body" style="left:17px;top:355px;width:300px">The benefit includes three protections in one: a cash value that grows at an average of 6% annually, a tax-free death benefit for your family, and long-term care coverage that pays 75% of your benefit upfront — tax-free — when you need care most.</p>
  <div class="abs photo" role="img" aria-label="Photo of a joyful older couple raising their arms while wading at the beach at sunset" style="left:325px;top:216px;width:164px;height:208px;background:linear-gradient(180deg,#cfc6bd 0%,#d9b48c 50%,#a6794f 100%)"></div>

  <div class="abs tier" style="left:10px">$1 / day → <span class="accent">$20,000</span></div>
  <div class="abs tier" style="left:169px">$2 / day → <span class="accent">$40,000</span></div>
  <div class="abs tier" style="left:327px">$3 / day → <span class="accent">$60,000</span></div>

  <div class="abs footer">
    <p class="tagline">Protect retirement. Preserve dignity. Plan ahead.</p>
    <p class="footer-sub">Whether you're single, married, with children or without —<br>there is protection in this plan for you.</p>
    <p class="cta">Look for your personalized offer. Coverage details are coming your way.</p>
    <p class="footer-note">Brokered by Orvane Benefits · Underwritten by TrelloraLife</p>
  </div>
</section>

</body>
</html>
```